Felmo - food stand (booth) design

We need posters for a small food stand situated in the centre of the city directly in front of a high-class shopping mall (see file 2 - the food stand at the square) . We sell cinnamon rolls which we named Felmo. We are looking for a design of the food stand which would lure the customer from the square in front of the mall of a size 30 meters (100 ft) wide. At the same time, it should be elegant, possibly Provence style in pastel colours.

We need the name and description of the product (meaning: Felmo – cinnamon rolls) to be visible from the front and maybe even the sides of the food stand. At the same time, we need to place the menu on some "wings", attached to the sides of the stand from outside. The menu will consist of 8 products (4 different kinds of Felmo rolls and 4 kinds of coffee). If you could visualize the wings, it would be nice.

We also need the design of the packaging of the product (a box similar to a hamburger box and a coffee cup) which might carry the logo (which we do not have), but again that is up to you. If you design the logo, maybe it should be placed on the outside of the food stand (up to you).

See the enclosed photos of the food stand from the front and the sides. The size of the food stand’s plan view is 2.5 x 2 meters (8.2 x 6.56 ft). The design can be either in the size of the current stickers (which would be replaced by yours) or it can cover the whole stand.

Below are sizes of the panels. We notice only the relevant ones
(for example the upper front is irrelevant, because it's always open, thus invisible). First is always x (eg. horizontal) axis. All sizes in centimeters.
A Front
A1 lower 234 x 40 cm
B Left side
B1 upper 174 x 100 cm
B2 lower 184 x 48 cm
C Right side (with the door)
C1 left 100 x 100 cm
C2 right (door) 48 x 184 cm

We are looking forward to your designs!

Thank you,
Team Felmo

```html
<!DOCTYPE html>
<html lang="en">
<head>
<meta charset="utf-8">
<title>Felmo – Food Stand Panels</title>
<link rel="stylesheet" href="https://fonts.googleapis.com/css2?family=Arimo:wght@400;700&family=Varela+Round&display=swap">
<style>
  :root {
    --backdrop: #ecebe8;
    --panel-light: #ead3ad;
    --panel-mid: #d7b486;
    --panel-dark: #c29a6b;
    --brand-red: #d90000;
    --text-light: #ffffff;
    --text-edge: #3a2a1a;
    --visual-tone: #c9996a;
  }
  * { margin: 0; padding: 0; box-sizing: border-box; }
  html, body {
    width: 1200px;
    height: 900px;
    overflow: hidden;
    background: var(--backdrop);
  }
  .canvas {
    position: relative;
    width: 1200px;
    height: 900px;
  }
  .panel {
    position: absolute;
    background:
      radial-gradient(ellipse at 20% 30%, rgba(255,255,255,0.25), transparent 60%),
      radial-gradient(ellipse at 85% 75%, rgba(120,80,40,0.18), transparent 55%),
      linear-gradient(135deg, var(--panel-mid), var(--panel-light) 45%, var(--panel-mid) 75%, var(--panel-dark));
  }
  .panel--upper {
    left: 45px; top: 50px;
    width: 1110px; height: 495px;
  }
  .panel--lower {
    left: 74px; top: 591px;
    width: 1052px; height: 207px;
  }
  .brand-name {
    position: absolute;
    font-family: "Arimo", Arial, sans-serif;
    font-weight: 700;
    color: var(--brand-red);
    line-height: 1;
    letter-spacing: 0.01em;
  }
  .panel--upper .brand-name {
    left: 40px; top: 22px;
    font-size: 212px;
  }
  .product-visual {
    position: absolute;
    left: 454px; top: 226px;
    width: 402px; height: 164px;
    border-radius: 12px;
    background: var(--visual-tone);
  }
  .tagline {
    position: absolute;
    font-family: "Arimo", Arial, sans-serif;
    color: var(--text-light);
    line-height: 1;
  }
  .panel--upper .tagline {
    left: 454px; top: 402px;
    font-size: 80px;
    -webkit-text-stroke: 1.5px var(--text-edge);
    text-shadow: 2px 2px 2px rgba(0,0,0,0.35);
  }
  .panel--lower .brand-name {
    left: 35px; top: 28px;
    font-size: 64px;
  }
  .panel--lower .tagline {
    left: 32px; top: 107px;
    font-size: 31px;
    font-family: "Varela Round", Arial, sans-serif;
    text-shadow: 1px 1px 1px rgba(0,0,0,0.45);
  }
  .menu-list {
    position: absolute;
    top: 28px;
    list-style: none;
    font-family: "Varela Round", Arial, sans-serif;
    font-size: 28px;
    line-height: 36px;
    color: var(--text-light);
    text-shadow: 1px 1px 1px rgba(0,0,0,0.45);
  }
  .menu-list--rolls { left: 425px; }
  .menu-list--coffee { left: 826px; top: 31px; }
</style>
</head>
<body>
  <main class="canvas">
    <section class="panel panel--upper">
      <h1 class="brand-name">FELMO</h1>
      <div class="product-visual" role="img" aria-label="Photo of two iced cinnamon rolls"></div>
      <p class="tagline">Cinnamon Rolls</p>
    </section>
    <section class="panel panel--lower">
      <h2 class="brand-name">FELMO</h2>
      <p class="tagline">Cinnamon Rolls</p>
      <ul class="menu-list menu-list--rolls">
        <li>Felmo roll kind 1</li>
        <li>Felmo roll kind 2</li>
        <li>Felmo roll kind 3</li>
        <li>Felmo roll kind 4</li>
      </ul>
      <ul class="menu-list menu-list--coffee">
        <li>Coffee kind 1</li>
        <li>Coffee kind 2</li>
        <li>Coffee kind 3</li>
        <li>Coffee kind 4</li>
      </ul>
    </section>
  </main>
</body>
</html>
```